Medical group practice

We need a flyer design incorporating the three doctors in the practice, there is a general practitioner, ophthalmologist and an obstetrician & Gynaecologist. see the attached file for the concept. will leave the colour design up to you

Target Market(s)

general public

Industry/Entity Type

Health Care

Colors

Designer to choose colors to be used in the design.

Requirements
Must have
• logos included in attachement

```html
<!DOCTYPE html>
<html lang="en">
<head>
<meta charset="utf-8">
<title>VitalCare Clinic – Our Doctors</title>
<link rel="stylesheet" href="https://fonts.googleapis.com/css2?family=Open+Sans:wght@400;600;700&family=Ubuntu:wght@400;500&family=Oswald:wght@500;600&family=Cinzel:wght@700&family=Tinos&display=swap">
<style>
  :root{
    --red:#c8202a;
    --green:#16994a;
    --green-text:#23a046;
    --yellow:#ffec00;
    --blue:#36ace2;
    --blue-text:#2ea6dd;
    --ink:#1d1d1d;
    --white:#fff;
  }
  *{margin:0;padding:0;box-sizing:border-box}
  html,body{width:848px;height:1200px;overflow:hidden;background:var(--white)}
  .flyer{position:relative;width:848px;height:1200px;overflow:hidden;font-family:"Open Sans",Arial,sans-serif;color:var(--ink)}
  .backdrop{position:absolute;inset:0}
  .abs{position:absolute}

  .brand{left:505px;top:36px;display:flex;align-items:center;gap:10px}
  .brand-dot{width:44px;height:44px;border-radius:50%;background:var(--red)}
  .brand-name{font-family:"Tinos",serif;font-size:21px;color:#222;letter-spacing:.3px}
  .tagline{left:605px;top:79px;font-family:Arial,sans-serif;font-size:14px;color:var(--red)}

  .hours{left:500px;top:246px;width:280px;text-align:center;font-family:"Ubuntu",sans-serif;color:#111;font-weight:500}
  .hours > div{height:44px;line-height:44px}
  .hours .day{font-size:23px;letter-spacing:.5px}
  .hours .time{font-size:36px}
  .hours .phone{font-size:18px;display:flex;align-items:center;justify-content:center;gap:8px}

  .doctor-badge{display:flex;align-items:center;justify-content:center;text-align:center;border-radius:50%;border:5px solid var(--red);font-weight:700;font-size:19px;line-height:1.25}
  .badge-gp{left:68px;top:371px;width:148px;height:148px;background:var(--green);color:var(--white)}
  .badge-eye{left:330px;top:433px;width:150px;height:150px;background:var(--yellow);color:var(--red)}
  .badge-obgyn{left:618px;top:498px;width:148px;height:148px;background:var(--blue);color:var(--white)}

  .credential{border:4px solid var(--red);background:var(--white);font-size:12.5px;color:#222;text-align:center;padding:5px 10px}
  .cred-gp{left:49px;top:519px;width:172px}
  .cred-eye{left:295px;top:582px;width:211px}
  .cred-obgyn{left:569px;top:632px;width:245px;line-height:1.45}

  .contact{font-size:11.5px;color:#222;line-height:20.5px}
  .contact li{list-style:none;display:flex;align-items:center;gap:9px}
  .contact svg{flex:none}
  .contact-gp{left:38px;top:570px}
  .contact-eye{left:300px;top:630px}
  .contact-obgyn{left:588px;top:702px}

  .services{list-style:none;font-size:14.5px;line-height:24.2px}
  .svc-gp{left:37px;top:692px;color:var(--green-text)}
  .svc-eye{left:299px;top:754px;color:var(--red)}
  .svc-obgyn{left:586px;top:824px;color:var(--blue-text)}

  .eye-reminder{left:35px;top:912px;width:210px;height:273px;border:4px solid #111;background:var(--white);padding:4px}
  .eye-reminder-inner{width:100%;height:100%;border:2px solid #111;background:linear-gradient(#f4f4f4,#e6e6e6);text-align:center;font-family:"Cinzel",serif;font-weight:700;padding-top:16px}
  .er-1{font-size:34px;line-height:1.05;color:#111}
  .er-2{font-size:22px;color:#111;margin-top:6px}
  .er-3{font-size:19px;color:var(--green);margin-top:10px}
  .er-4{font-size:17px;color:var(--red);margin-top:10px}
  .er-5{font-size:14px;color:#111;margin-top:10px}
  .er-6{font-size:12.5px;color:#111;margin-top:14px}
  .er-7{font-size:10px;color:#111;margin-top:12px}

  .offer{left:262px;top:1088px;width:548px;height:60px;line-height:60px;text-align:center;font-family:"Oswald",sans-serif;font-weight:600;color:var(--white);font-size:30px;white-space:nowrap}
  .offer .free{font-size:48px;margin:0 12px;vertical-align:-2px}
  .offer-phone{left:272px;top:1146px;width:528px;text-align:center;color:var(--white);font-size:16px}
</style>
</head>
<body>
<div class="flyer">
  <svg class="backdrop" width="848" height="1200" viewBox="0 0 848 1200">
    <defs>
      <linearGradient id="photoTone" x1="0" y1="0" x2="1" y2="1">
        <stop offset="0" stop-color="#d9dde3"/>
        <stop offset=".45" stop-color="#bcc7d4"/>
        <stop offset=".7" stop-color="#e9edf2"/>
        <stop offset="1" stop-color="#cfd6df"/>
      </linearGradient>
    </defs>
    <rect role="img" aria-label="Photo of a smiling nurse in blue scrubs with a stethoscope in a hospital ward" x="0" y="0" width="848" height="640" fill="url(#photoTone)"/>
    <polygon points="0,0 848,0 848,150 0,22" fill="#fff"/>
    <polygon points="410,92 848,148 848,232" fill="var(--yellow)"/>
    <polygon points="0,395 848,555 848,625 0,445" fill="var(--green)"/>
    <polygon points="0,445 848,625 848,1200 0,1200" fill="#fff"/>
    <polygon points="0,890 848,1080 848,1200 0,1200" fill="var(--red)"/>
    <line x1="264" y1="500" x2="264" y2="890" stroke="var(--red)" stroke-width="2"/>
    <line x1="538" y1="565" x2="538" y2="1010" stroke="var(--red)" stroke-width="2"/>
    <line x1="86" y1="663" x2="262" y2="663" stroke="var(--red)" stroke-width="1.5"/>
    <line x1="346" y1="725" x2="536" y2="725" stroke="var(--red)" stroke-width="1.5"/>
    <line x1="632" y1="795" x2="848" y2="795" stroke="var(--red)" stroke-width="1.5"/>
    <circle cx="62" cy="663" r="22" fill="#fff" stroke="var(--red)" stroke-width="2.5"/>
    <path d="M57 652h10v6h6v10h-6v6H57v-6h-6v-10h6z" fill="#3a8fd0"/>
    <circle cx="322" cy="725" r="22" fill="#fff" stroke="var(--red)" stroke-width="2.5"/>
    <path d="M306 726q16-14 32 0q-16 12-32 0z" fill="none" stroke="#6a2a8a" stroke-width="2"/>
    <circle cx="322" cy="726" r="4.5" fill="#2e9fd8"/>
    <circle cx="608" cy="795" r="22" fill="#fff" stroke="var(--red)" stroke-width="2.5"/>
    <circle cx="602" cy="789" r="6" fill="#2a6fb8"/>
    <circle cx="615" cy="797" r="5" fill="var(--green)"/>
    <path d="M592 808q10-12 22 0" fill="none" stroke="#2a6fb8" stroke-width="3"/>
    <line x1="278" y1="1078" x2="495" y2="1078" stroke="#fff" stroke-width="1.5"/>
    <line x1="576" y1="1078" x2="795" y2="1078" stroke="#fff" stroke-width="1.5"/>
    <g fill="none" stroke="#fff" stroke-width="3">
      <path d="M505 1071h24l-2 12q-1 6-10 6t-10-6z"/>
      <path d="M541 1071h24l-2 12q-1 6-10 6t-10-6z"/>
      <path d="M529 1073q6-4 12 0"/>
    </g>
  </svg>

  <div class="abs brand"><span class="brand-dot"></span><span class="brand-name">VITALCARE CLINIC</span></div>
  <div class="abs tagline">Your Health is our Priority</div>

  <div class="abs hours">
    <div class="day">MONDAY – FRIDAYS</div>
    <div class="time">9AM-6PM</div>
    <div class="day">SATURDAYS</div>
    <div class="time">10AM-5PM</div>
    <div class="phone">
      <svg width="14" height="14" viewBox="0 0 24 24"><path d="M6.6 10.8a15 15 0 0 0 6.6 6.6l2.2-2.2a1 1 0 0 1 1-.25 11.4 11.4 0 0 0 3.6.57 1 1 0 0 1 1 1V20a1 1 0 0 1-1 1A17 17 0 0 1 3 4a1 1 0 0 1 1-1h3.5a1 1 0 0 1 1 1c0 1.25.2 2.45.57 3.57a1 1 0 0 1-.25 1z" fill="var(--red)"/></svg>
      (555) 640 3380 / 3381
    </div>
  </div>

  <div class="abs doctor-badge badge-gp">Dr.<br>Marcus<br>Holloway</div>
  <div class="abs doctor-badge badge-eye">Dr.<br>Isabela<br>R. Fuentes</div>
  <div class="abs doctor-badge badge-obgyn">Dr.<br>Kiran<br>Malhotra</div>

  <div class="abs credential cred-gp">MD,General Practitioner</div>
  <div class="abs credential cred-eye">MD. Surgeon Ophthalmologist</div>
  <div class="abs credential cred-obgyn">BMedSci, MBBS, DM (O&amp;G), FACOG<br>Obstetrician &amp; Gynaecologist</div>

  <ul class="abs contact contact-gp">
    <li><svg width="11" height="11" viewBox="0 0 24 24"><path d="M6.6 10.8a15 15 0 0 0 6.6 6.6l2.2-2.2a1 1 0 0 1 1-.25 11.4 11.4 0 0 0 3.6.57 1 1 0 0 1 1 1V20a1 1 0 0 1-1 1A17 17 0 0 1 3 4a1 1 0 0 1 1-1h3.5a1 1 0 0 1 1 1c0 1.25.2 2.45.57 3.57a1 1 0 0 1-.25 1z" fill="var(--green)"/></svg>(555) 210 4417</li>
    <li><svg width="12" height="10" viewBox="0 0 24 18"><rect width="24" height="18" rx="2" fill="var(--green)"/><path d="M1 2l11 8 11-8" fill="none" stroke="#fff" stroke-width="2"/></svg>m.holloway.doc@mail.com</li>
    <li><svg width="10" height="13" viewBox="0 0 20 26"><path d="M10 0a10 10 0 0 1 10 10c0 7-10 16-10 16S0 17 0 10A10 10 0 0 1 10 0z" fill="var(--green)"/><circle cx="10" cy="10" r="4" fill="#fff"/></svg>42 Harbour Road, Port Elms, Lindara</li>
  </ul>
  <ul class="abs contact contact-eye">
    <li><svg width="11" height="11" viewBox="0 0 24 24"><path d="M6.6 10.8a15 15 0 0 0 6.6 6.6l2.2-2.2a1 1 0 0 1 1-.25 11.4 11.4 0 0 0 3.6.57 1 1 0 0 1 1 1V20a1 1 0 0 1-1 1A17 17 0 0 1 3 4a1 1 0 0 1 1-1h3.5a1 1 0 0 1 1 1c0 1.25.2 2.45.57 3.57a1 1 0 0 1-.25 1z" fill="var(--red)"/></svg>(555) 318 2290</li>
    <li><svg width="12" height="10" viewBox="0 0 24 18"><rect width="24" height="18" rx="2" fill="var(--red)"/><path d="M1 2l11 8 11-8" fill="none" stroke="#fff" stroke-width="2"/></svg>isabela.doct@mail.com</li>
    <li><svg width="10" height="13" viewBox="0 0 20 26"><path d="M10 0a10 10 0 0 1 10 10c0 7-10 16-10 16S0 17 0 10A10 10 0 0 1 10 0z" fill="var(--red)"/><circle cx="10" cy="10" r="4" fill="#fff"/></svg>42 Harbour Road, Port Elms, Lindara</li>
  </ul>
  <ul class="abs contact contact-obgyn">
    <li><svg width="11" height="11" viewBox="0 0 24 24"><path d="M6.6 10.8a15 15 0 0 0 6.6 6.6l2.2-2.2a1 1 0 0 1 1-.25 11.4 11.4 0 0 0 3.6.57 1 1 0 0 1 1 1V20a1 1 0 0 1-1 1A17 17 0 0 1 3 4a1 1 0 0 1 1-1h3.5a1 1 0 0 1 1 1c0 1.25.2 2.45.57 3.57a1 1 0 0 1-.25 1z" fill="var(--blue)"/></svg>(555) 402 7716 / (555) 893 1248</li>
    <li><svg width="12" height="10" viewBox="0 0 24 18"><rect width="24" height="18" rx="2" fill="var(--blue)"/><path d="M1 2l11 8 11-8" fill="none" stroke="#fff" stroke-width="2"/></svg>drmalhotra@mail.com</li>
    <li><svg width="10" height="13" viewBox="0 0 20 26"><path d="M10 0a10 10 0 0 1 10 10c0 7-10 16-10 16S0 17 0 10A10 10 0 0 1 10 0z" fill="var(--blue)"/><circle cx="10" cy="10" r="4" fill="#fff"/></svg>42 Harbour Road, Port Elms, Lindara</li>
  </ul>

  <ul class="abs services svc-gp">
    <li>General Checks</li>
    <li>Annual Check ups</li>
    <li>Wound Care/Dressings</li>
    <li>Incision &amp; Drainage</li>
    <li>Suturing lacerations</li>
    <li>Pain Injections</li>
    <li>Glucose checks</li>
    <li>Foreign Body Removal</li>
  </ul>
  <ul class="abs services svc-eye">
    <li>Eyes disease examination</li>
    <li>Surgery of Pterygium</li>
    <li>Cataract</li>
    <li>Glaucoma</li>
    <li>Emergency: Conjunctivitis</li>
    <li>Traumatism</li>
    <li>Foreign body and more</li>
  </ul>
  <ul class="abs services svc-obgyn">
    <li>Obstetrics: Prenatal Care</li>
    <li>Delivery, Postnatal checks</li>
    <li>High Risk pregnancy</li>
    <li>Gynaecology : Pap smears</li>
    <li>Abnormal vaginal bleeding</li>
    <li>Fibroids, Colposcopy</li>
    <li>Family planning, Infertility</li>
    <li>Cancer screening and more</li>
  </ul>

  <div class="abs eye-reminder">
    <div class="eye-reminder-inner">
      <div class="er-1">Get</div>
      <div class="er-2">YOUR EYES</div>
      <div class="er-3">CHECKED</div>
      <div class="er-4">EVERY YEAR,</div>
      <div class="er-5">WHETHER YOU</div>
      <div class="er-6">WEAR GLASSES</div>
      <div class="er-7">OR NOT</div>
    </div>
  </div>

  <div class="abs offer">Book a<span class="free">FREE</span>Eye-Health Checkup today!</div>
  <div class="abs offer-phone">(555)318 2290</div>
</div>
</body>
</html>
```